Wade Merriton Professional Coaching

I would like a website with a mountain theme geared towards professional executives reaching higher peaks and goals. This is a 3 page website with brand essence information on the opening page, the coaching process on a second page and "about me" and lead capture form on a third page

Target Market(s)

C-Level audience, involved in tech, government, manufacturing, and transportation type of corporations

Coding

Number of Pages Required

3 page

Font styles to use
Sans Serif

Colors
a7a7a7
1b1b1b
e8e8e8
3176b5
abd036
0355a3

Requirements
Must have
• Looking for a user friendly site that I can manage/update going forward. Must have:
• 1. "Is coaching right for you?" - page 1
• 2. "Our Process" page 2 - I will describe how we approach coaching
• 3. "Contact us" page 3 where I can capture contact information from potential clients
• 4. Clean and professional with more modern font
• 5. Links to personal social media sites
• 6. Ability to upload/download .pdf documents as resources
• 7. Ability to add on new pages in the future (such as a blog page)
Nice to have
• I want a place to store articles I write or use.
• LinkedIn or Twitter Feed
Should not have
• Not fluffy or too 'zen' like personal life coaches tend to present.

```html
<!DOCTYPE html>
<html lang="en">
<head>
<meta charset="utf-8">
<title>Wade Merriton Professional Coaching</title>
<link href="https://fonts.googleapis.com/css2?family=Jost:wght@400;500;600;700&display=swap" rel="stylesheet">
<style>
:root{
  --blue:#3176b5;
  --blue-deep:#0355a3;
  --ink:#1b1b1b;
  --grey:#a7a7a7;
  --mist:#e8e8e8;
  --white:#ffffff;
  --body:#444444;
}
*{box-sizing:border-box;margin:0;padding:0}
html,body{width:1200px;height:3607px;overflow:hidden}
body{font-family:"Jost",Arial,sans-serif;color:var(--ink);background:var(--white);position:relative}
p{line-height:1.55}

/* header */
.site-header{position:absolute;left:0;top:0;width:1200px;height:101px;background:var(--white)}
.brand{position:absolute;left:142px;top:36px;text-align:center}
.brand-name{font-size:30px;font-weight:500;letter-spacing:1px;color:var(--ink);line-height:1}
.brand-tag{font-size:10px;font-weight:500;letter-spacing:3px;color:var(--ink);margin-top:5px}
.topbar{position:absolute;top:10px;right:140px;display:flex;gap:26px;font-size:13px;color:var(--ink)}
.topbar span{display:flex;align-items:center;gap:7px}
.main-nav{position:absolute;top:58px;left:478px;display:flex;font-size:13px;font-weight:500}
.main-nav a{display:block;padding:0 18px;height:43px;line-height:26px;color:var(--ink);text-decoration:none;white-space:nowrap}
.main-nav a.active{color:var(--blue);border-bottom:4px solid var(--blue)}
.social{display:flex;gap:8px}
.social i{display:block;width:28px;height:28px;background:var(--blue)}
.header-social{position:absolute;top:56px;left:958px}

/* hero */
.hero{position:absolute;left:0;top:101px;width:1200px;height:565px;
  background:linear-gradient(160deg,#6f8fc4 0%,#b8c8e4 30%,#eef2f8 50%,#a9bad6 75%,#7f92b5 100%)}
.hero-title{position:absolute;right:145px;top:195px;text-align:right;line-height:1.05;color:var(--ink)}
.hero-title .light{font-size:68px;font-weight:400;display:block}
.hero-title .bold{font-size:58px;font-weight:600;display:block}
.hero-text{position:absolute;right:145px;top:338px;width:420px;text-align:right;font-size:15px;font-weight:500;color:var(--ink)}
.btn{display:inline-block;background:var(--blue);color:var(--white);font-size:15px;text-align:center;border-radius:2px}
.hero-btn{position:absolute;left:943px;top:411px;width:115px;height:35px;line-height:35px}
.slider-dots{position:absolute;left:570px;top:502px;display:flex;gap:8px}
.slider-dots i{display:block;width:14px;height:14px;background:#596a7a}
.slider-dots i.on{background:var(--blue)}

/* about */
.about{position:absolute;left:0;top:666px;width:1200px;height:601px;
  background:linear-gradient(180deg,#ffffff 0%,#f2f3f5 40%,#e1e4e8 75%,#ffffff 100%)}
.portrait-ring{position:absolute;left:157px;top:59px;width:432px;height:432px;border-radius:50%;
  border:9px solid var(--ink);border-top-color:var(--blue);border-left-color:var(--blue)}
.portrait{position:absolute;left:10px;top:10px;width:394px;height:394px;border-radius:50%;
  background:linear-gradient(150deg,#5f8a48 0%,#3c5f33 40%,#263a5a 70%,#1d2c4a 100%)}
.section-heading{font-size:46px;font-weight:600;color:var(--ink)}
.about-heading{position:absolute;left:623px;top:120px}
.about-body{position:absolute;left:623px;top:218px;width:437px;font-size:12.5px;color:var(--body);text-align:justify}
.about-body p+p{margin-top:6px}
.about-body .lead{font-weight:600;color:var(--ink)}
.about-btn{position:absolute;left:623px;top:452px;width:112px;height:38px;line-height:38px}

/* programs */
.programs{position:absolute;left:0;top:1267px;width:1200px;height:758px;background:var(--white)}
.centre-heading{position:absolute;left:0;width:1200px;text-align:center}
.rule{position:absolute;left:570px;width:60px;height:4px;background:var(--blue)}
.intro{position:absolute;left:320px;width:560px;text-align:center;font-size:13px;color:var(--ink)}
.program-card{position:absolute;top:248px;width:296px;height:410px}
.program-card .edge{position:absolute;left:0;top:0;width:210px;height:8px;background:var(--blue)}
.program-card .edge-side{position:absolute;left:0;top:0;width:8px;height:120px;background:var(--blue)}
.program-card .shadow{position:absolute;left:14px;top:14px;right:-12px;bottom:-12px;background:var(--ink)}
.program-card .face{position:absolute;left:8px;top:8px;right:0;bottom:0;background:#eeeeee}
.program-card .photo{position:absolute;left:8px;top:8px;right:8px;height:190px;background:linear-gradient(135deg,#c9c2b6,#7a8590 55%,#3f4b57)}
.program-card h3{position:absolute;left:0;right:0;top:218px;text-align:center;font-size:19px;font-weight:600;color:var(--blue)}
.program-card p{position:absolute;left:26px;right:18px;top:250px;text-align:center;font-size:13px;color:var(--body)}
.program-card .more{position:absolute;left:50%;margin-left:-10px;top:362px;width:28px;height:28px;background:#cfcfcf}

/* testimonial */
.testimonial{position:absolute;left:0;top:2025px;width:1200px;height:500px}
.testimonial .tab{position:absolute;left:0;top:0;width:577px;height:38px;background:var(--blue);clip-path:polygon(0 0,100% 0,96% 100%,0 100%)}
.testimonial .scene{position:absolute;left:0;top:38px;width:1200px;height:424px;
  background:linear-gradient(180deg,#2c4a78 0%,#5d7ea6 45%,#7b8fa3 65%,#3e4a55 100%)}
.testimonial .slant{position:absolute;right:0;top:462px;width:600px;height:38px;background:var(--ink);clip-path:polygon(6% 0,100% 0,100% 100%,0 100%)}
.quote-mark{position:absolute;left:449px;top:142px}
.quote-text{position:absolute;left:449px;top:182px;width:518px;font-size:12px;color:var(--white);text-align:justify;line-height:1.5;text-indent:76px}
.quote-name{position:absolute;left:460px;top:340px;font-size:15px;color:var(--white)}
.quote-role{position:absolute;left:470px;top:362px;font-size:12px;color:var(--white)}
.quote-arrows{position:absolute;left:1034px;top:202px}
.quote-arrows i{display:block;width:22px;height:22px;border:1px solid var(--white);margin-bottom:6px}

/* learning */
.learning{position:absolute;left:0;top:2525px;width:1200px;height:505px;background:var(--white)}
.post{position:absolute;width:440px;height:120px}
.post .thumb{position:absolute;left:0;top:0;width:115px;height:115px;border:3px solid #cfcfcf;background:linear-gradient(135deg,#b9a58f,#6b7b8c 60%,#3a4a5c)}
.post h4{position:absolute;left:137px;top:0;font-size:18px;font-weight:500;color:var(--ink)}
.post .date{position:absolute;left:137px;top:27px;font-size:13px;color:var(--blue)}
.post p{position:absolute;left:137px;top:47px;width:300px;font-size:12.5px;color:var(--body)}
.post p b{font-weight:400;color:var(--blue)}
.pager{position:absolute;left:575px;display:flex;gap:4px}
.pager i{display:block;width:22px;height:22px;border:1px solid #888}

/* newsletter + footer */
.newsletter{position:absolute;left:0;top:3000px;width:1200px;height:562px;
  background:linear-gradient(180deg,#ffffff 0%,#f3f1ee 18%,#e5c9a8 40%,#b7744a 55%,#3e4456 72%,#121d33 100%)}
.news-heading{top:175px;font-size:44px}
.news-form{position:absolute;left:293px;top:290px;width:614px;height:48px;display:flex}
.news-form .field{flex:0 0 460px;background:var(--white);font-size:13px;color:#555;padding:0 14px;line-height:48px}
.news-form .submit{flex:1;background:var(--blue);color:var(--white);font-size:16px;text-align:center;line-height:48px}
.contact-item{position:absolute;top:433px;display:flex;gap:22px;font-size:11.5px;color:var(--white);line-height:1.4}
.contact-item .icon{width:34px;height:34px;border-radius:50%;background:var(--blue);display:flex;align-items:center;justify-content:center;flex:none}
.footer-nav{position:absolute;left:0;width:1200px;top:521px;display:flex;justify-content:center;gap:44px;font-size:14px;color:var(--white)}
.bottom-bar{position:absolute;left:0;top:3562px;width:1200px;height:45px;background:#121a2a}
.bottom-bar .copy{position:absolute;left:142px;top:14px;font-size:12px;color:var(--mist)}
.bottom-bar .social{position:absolute;left:958px;top:8px}
</style>
</head>
<body>

<header class="site-header">
  <div class="brand">
    <div class="brand-name">WADE MERRITON</div>
    <div class="brand-tag">PROFESSIONAL COACHING</div>
  </div>
  <div class="topbar">
    <span><svg width="14" height="14" viewBox="0 0 14 14"><rect x="0.5" y="0.5" width="13" height="13" fill="none" stroke="#1b1b1b"/><path d="M4 3.5l1.5 2-1 1c.6 1.3 1.7 2.4 3 3l1-1 2 1.5-1 1.5C6 11 3 8 2.5 4.5z" fill="#1b1b1b"/></svg>123 456 7890</span>
    <span><svg width="14" height="14" viewBox="0 0 14 14"><rect x="0.5" y="2.5" width="13" height="9" fill="none" stroke="#1b1b1b"/><path d="M1 3l6 5 6-5" fill="none" stroke="#1b1b1b"/></svg>info@merriton.com</span>
  </div>
  <nav class="main-nav">
    <a class="active">HOME</a><a>ABOUT ME</a><a>COACHING PROCESS</a><a>CONTACT</a>
  </nav>
  <div class="social header-social"><i></i><i></i><i></i></div>
</header>

<section class="hero" role="img" aria-label="Climbers roped together ascending a snowy mountain ridge under a blue sky">
  <h1 class="hero-title"><span class="light">Reach Your</span><span class="bold">Leadership Peak</span></h1>
  <p class="hero-text">Lorem ipsum dolor sit amet, consectetuer adipiscing elit, euismod tincidunt ut laoreet dolore magna aliquam.</p>
  <a class="btn hero-btn">Read More</a>
  <div class="slider-dots"><i class="on"></i><i></i><i></i></div>
</section>

<section class="about">
  <div class="portrait-ring">
    <div class="portrait" role="img" aria-label="Portrait of the coach in a navy blazer, outdoors"></div>
  </div>
  <h2 class="section-heading about-heading">About Me</h2>
  <div class="about-body">
    <p class="lead">Lorem ipsum dolor sit amet, consectetuer adipiscing elit, sed diam nonum my nibh euismod tincidunt ut laoreet dolore magna aliquam.</p>
    <p>Lorem ipsum dolor sit amet, consectetuer adipiscing elit, sed diam nonummy nibh euismod tincidunt ut laoreet dolore magna aliquam erat volutpat. Ut wisi enim ad minim veniam, quis nostrud exerci tation ullamcorper suscipit lobortis nisl ut aliquip ex ea commodo consequat. Duis autem vel eum iriure dolor in hendrerit in vulputate velit esse molestie consequat, vel illum dolore eu feugiat nulla facilisis at vero eros et accumsan et iusto odio dignissim qui blandit praesent.</p>
  </div>
  <a class="btn about-btn">Read More</a>
</section>

<section class="programs">
  <h2 class="section-heading centre-heading" style="top:92px;font-size:40px">Coaching Programs</h2>
  <div class="rule" style="top:162px"></div>
  <p class="intro" style="top:178px">Lorem ipsum dolor sit amet, consectetuer adipiscing elit, sed diam nonum my nibh euismod tincidunt ut laoreet dolore magna aliquam.</p>

  <article class="program-card" style="left:137px">
    <div class="shadow"></div><div class="edge"></div><div class="edge-side"></div><div class="face"></div>
    <div class="photo" role="img" aria-label="Team gathered around a meeting table"></div>
    <h3>Consectetuer Adipiscing</h3>
    <p>Lorem ipsum dolor sit amet, consectetuer adipiscing elit, sed diam nonummy nibh euismod tincidunt ut laoreet dolore magna aliquam erat volutpat.</p>
    <div class="more"><svg width="28" height="28" viewBox="0 0 28 28"><path d="M14 8v12M8 14h12" stroke="#fff" stroke-width="3"/></svg></div>
  </article>

  <article class="program-card" style="left:457px">
    <div class="shadow"></div><div class="edge"></div><div class="edge-side"></div><div class="face"></div>
    <div class="photo" role="img" aria-label="Workshop group working together at a table"></div>
    <h3>Consectetuer Adipiscing</h3>
    <p>Lorem ipsum dolor sit amet, consectetuer adipiscing elit, sed diam nonummy nibh euismod tincidunt ut laoreet dolore magna aliquam erat volutpat.</p>
    <div class="more"><svg width="28" height="28" viewBox="0 0 28 28"><path d="M14 8v12M8 14h12" stroke="#fff" stroke-width="3"/></svg></div>
  </article>

  <article class="program-card" style="left:770px">
    <div class="shadow"></div><div class="edge"></div><div class="edge-side"></div><div class="face"></div>
    <div class="photo" role="img" aria-label="Audience attending a seminar presentation"></div>
    <h3>Consectetuer Adipiscing</h3>
    <p>Lorem ipsum dolor sit amet, consectetuer adipiscing elit, sed diam nonummy nibh euismod tincidunt ut laoreet dolore magna aliquam erat volutpat.</p>
    <div class="more"><svg width="28" height="28" viewBox="0 0 28 28"><path d="M14 8v12M8 14h12" stroke="#fff" stroke-width="3"/></svg></div>
  </article>
</section>

<section class="testimonial">
  <div class="tab"></div>
  <div class="scene" role="img" aria-label="Person with outstretched arms standing on a rocky summit above misty mountain ranges"></div>
  <div class="slant"></div>
  <svg class="quote-mark" width="62" height="44" viewBox="0 0 70 50"><path d="M0 50V25C0 10 8 2 24 0v10c-7 2-10 6-10 13h10v27zM38 50V25C38 10 46 2 62 0v10c-7 2-10 6-10 13h10v27z" fill="#ffffff" opacity="0.85"/></svg>
  <p class="quote-text">Lorem ipsum dolor sit amet, consectetuer adipiscing elit, sed diam nonummy nibh euismod tincidunt ut laoreet dolore magna aliquam erat volutpat. Ut wisi enim ad minim veniam, quis nostrud exerci tation ullamcorper suscipit lobortis nisl ut aliquip ex ea commodo consequat. Duis autem vel eum iriure dolor in hendrerit in vulputate velit esse molestie consequat, vel illum dolore eu feugiat nulla facilisis at vero eros et accumsan et iusto odio dignissim qui blandit praesent</p>
  <div class="quote-name">- Alden Voss</div>
  <div class="quote-role">Adipiscing Elit, Sed Diam</div>
  <div class="quote-arrows">
    <i><svg width="20" height="20" viewBox="0 0 20 20"><path d="M5 12l5-5 5 5" fill="none" stroke="#fff" stroke-width="1.5"/></svg></i>
    <i><svg width="20" height="20" viewBox="0 0 20 20"><path d="M5 8l5 5 5-5" fill="none" stroke="#fff" stroke-width="1.5"/></svg></i>
  </div>
</section>

<section class="learning">
  <h2 class="section-heading centre-heading" style="top:85px;font-size:40px">Learning Journey</h2>
  <div class="rule" style="top:153px"></div>

  <article class="post" style="left:142px;top:217px">
    <div class="thumb" role="img" aria-label="Colleagues reviewing documents together"></div>
    <h4>Consectetuer Adipiscing Elit Sed…</h4><div class="date">13 Feb 2019</div>
    <p>Lorem ipsum dolor sit amet, consectetuer adipiscing elit, sed diam nonummy nibh euismod tincidunt ut laoreet dolore magna aliquam. <b>[+]</b></p>
  </article>
  <article class="post" style="left:620px;top:217px">
    <div class="thumb" role="img" aria-label="Colleagues reviewing documents together"></div>
    <h4>Consectetuer Adipiscing Elit Sed…</h4><div class="date">13 Feb 2019</div>
    <p>Lorem ipsum dolor sit amet, consectetuer adipiscing elit, sed diam nonummy nibh euismod tincidunt ut laoreet dolore magna aliquam. <b>[+]</b></p>
  </article>
  <article class="post" style="left:142px;top:361px">
    <div class="thumb" role="img" aria-label="Presenter speaking to a seated team"></div>
    <h4>Consectetuer Adipiscing Elit Sed…</h4><div class="date">10 Feb 2019</div>
    <p>Lorem ipsum dolor sit amet, consectetuer adipiscing elit, sed diam nonummy nibh euismod tincidunt ut laoreet dolore magna aliquam erat volutpat. <b>[+]</b></p>
  </article>
  <article class="post" style="left:620px;top:361px">
    <div class="thumb" role="img" aria-label="Presenter speaking to a seated team"></div>
    <h4>Consectetuer Adipiscing Elit Sed…</h4><div class="date">10 Feb 2019</div>
    <p>Lorem ipsum dolor sit amet, consectetuer adipiscing elit, sed diam nonummy nibh euismod tincidunt ut laoreet dolore magna aliquam erat volutpat. <b>[+]</b></p>
  </article>
</section>

<section class="newsletter" role="img" aria-label="Mountain peaks lit orange at sunrise fading into a dark night sky">
  <div class="pager" style="top:78px">
    <i><svg width="20" height="20" viewBox="0 0 20 20"><path d="M12 5l-5 5 5 5" fill="none" stroke="#666" stroke-width="1.5"/></svg></i>
    <i style="border-color:#ccc"><svg width="20" height="20" viewBox="0 0 20 20"><path d="M8 5l5 5-5 5" fill="none" stroke="#ccc" stroke-width="1.5"/></svg></i>
  </div>
  <h2 class="section-heading centre-heading news-heading">Subscribe Newsletter</h2>
  <div class="rule" style="top:240px"></div>
  <div class="news-form"><div class="field">Enter Your Email Address</div><div class="submit">Sign Up</div></div>

  <div class="contact-item" style="left:288px">
    <span class="icon"><svg width="16" height="16" viewBox="0 0 16 16"><path d="M8 1a5 5 0 0 1 5 5c0 4-5 9-5 9S3 10 3 6a5 5 0 0 1 5-5z" fill="#fff"/><circle cx="8" cy="6" r="2" fill="#3176b5"/></svg></span>
    <span>Building, 1234 City Road,<br>Area Country - US</span>
  </div>
  <div class="contact-item" style="left:536px">
    <span class="icon"><svg width="16" height="16" viewBox="0 0 16 16"><path d="M4 1.5l2.5 3-1.5 1.5c.8 2 2.3 3.5 4.3 4.3L10.8 8.8l3 2.5-1.5 2.5C7 13.5 2.5 9 2.2 3.5z" fill="#fff"/></svg></span>
    <span>Phone<br>+123-456-7890</span>
  </div>
  <div class="contact-item" style="left:748px">
    <span class="icon"><svg width="16" height="16" viewBox="0 0 16 16"><rect x="1.5" y="3.5" width="13" height="9" fill="none" stroke="#fff" stroke-width="1.3"/><path d="M2 4l6 5 6-5" fill="none" stroke="#fff" stroke-width="1.3"/></svg></span>
    <span>Email<br>info@merriton.com</span>
  </div>

  <nav class="footer-nav"><span>HOME</span><span>OUR PROCESS</span><span>ABOUT ME</span><span>CONTACT US</span></nav>
</section>

<footer class="bottom-bar">
  <div class="copy">Copyright © 2019 Merriton. All Rights Reserved.</div>
  <div class="social"><i></i><i></i><i></i></div>
</footer>

</body>
</html>
```